To design a illustration tattoo expo poster, Please think about Shanghai is a fashion & modern city, A1 size, poster text below:

2016上海国际墨影狂潮艺术展
Shanghai Inkwave Frenzy & Skin Craft Expo

日期 Date: 9/2-9/4

地点:上海国际锦澜会馆
Venue: Shanghai International Brocade Hall

http://www.inkwavefrenzyfair.example
Email: expo@inkwave-frenzy.example

Target Market(s)

Shanghai, China

Industry/Entity Type

Fashion

Requirements
Must have
• My Project have to design by illustration, and need ai file and font, the text have to provide non-create outline & create outline both file.

```html
<!DOCTYPE html>
<html lang="zh">
<head>
<meta charset="utf-8">
<title>2016 Shanghai Inkwave Frenzy &amp; Skin Craft Expo</title>
<link href="https://fonts.googleapis.com/css2?family=Bebas+Neue&family=Noto+Sans+SC:wght@300;400&family=Open+Sans:wght@400&display=swap" rel="stylesheet">
<style>
  :root {
    --bg-blue: #3f6290;
    --bg-blue-dark: #395a85;
    --text-light: #f3f3f1;
    --text-soft: #e4e6ec;
    --ring-grey: #6d7472;
    --badge-line: #111111;
    --badge-fill: #a3a49f;
    --star: #dcd9cf;
    --art-orange: #f39422;
    --art-yellow: #dde63a;
    --art-cyan: #6fc9d4;
  }
  html, body {
    margin: 0;
    padding: 0;
    width: 846px;
    height: 1200px;
    overflow: hidden;
    background: var(--bg-blue);
  }
  .poster {
    display: block;
    width: 846px;
    height: 1200px;
  }
  .display-type {
    font-family: "Bebas Neue", "Arial Narrow", sans-serif;
    fill: var(--text-light);
    filter: drop-shadow(1px 2px 1px rgba(0,0,0,0.35));
  }
  .cjk-type {
    font-family: "Noto Sans SC", sans-serif;
    font-weight: 300;
    fill: var(--text-light);
  }
  .contact-type {
    font-family: "Open Sans", sans-serif;
    font-size: 22px;
    fill: var(--text-soft);
  }
  .badge-ring { fill: var(--ring-grey); stroke: var(--badge-line); stroke-width: 5; }
  .badge-outline { fill: none; stroke: var(--badge-line); stroke-width: 6; }
  .badge-star { fill: var(--star); }
</style>
</head>
<body>
<svg class="poster" viewBox="0 0 846 1200" width="846" height="1200" xmlns="http://www.w3.org/2000/svg">
  <defs>
    <radialGradient id="bg-tone" cx="50%" cy="45%" r="75%">
      <stop offset="0" stop-color="#41648f"/>
      <stop offset="1" stop-color="#3a5a86"/>
    </radialGradient>
    <filter id="paper-grain" x="0" y="0" width="100%" height="100%">
      <feTurbulence type="fractalNoise" baseFrequency="0.9" numOctaves="2" result="noise"/>
      <feColorMatrix type="matrix" values="0 0 0 0 0  0 0 0 0 0  0 0 0 0 0  0 0 0 0.10 0"/>
    </filter>
    <radialGradient id="art-hand" cx="50%" cy="50%" r="50%">
      <stop offset="0" stop-color="var(--art-orange)"/>
      <stop offset="0.6" stop-color="var(--art-orange)" stop-opacity="0.85"/>
      <stop offset="1" stop-color="var(--art-orange)" stop-opacity="0"/>
    </radialGradient>
    <radialGradient id="art-machine" cx="50%" cy="50%" r="50%">
      <stop offset="0" stop-color="var(--art-cyan)"/>
      <stop offset="0.45" stop-color="var(--art-yellow)" stop-opacity="0.9"/>
      <stop offset="1" stop-color="var(--art-yellow)" stop-opacity="0"/>
    </radialGradient>
    <clipPath id="badge-window">
      <circle cx="422" cy="678" r="240"/>
    </clipPath>
    <path id="star-shape" d="M0,-11 L2.6,-3.6 L10.5,-3.4 L4.2,1.4 L6.5,8.9 L0,4.4 L-6.5,8.9 L-4.2,1.4 L-10.5,-3.4 L-2.6,-3.6 Z"/>
  </defs>

  <rect class="background" width="846" height="1200" fill="url(#bg-tone)"/>
  <rect class="background-grain" width="846" height="1200" filter="url(#paper-grain)"/>

  <!-- Headline -->
  <g class="headline">
    <text class="display-type year" x="46" y="172" font-size="152" textLength="218" lengthAdjust="spacingAndGlyphs">2016</text>
    <text class="cjk-type title-cn" x="272" y="142" font-size="44" textLength="536" lengthAdjust="spacingAndGlyphs">上海国际墨影狂潮艺术展</text>
    <text class="display-type city" x="36" y="244" font-size="72" textLength="230" lengthAdjust="spacingAndGlyphs">SHANGHAI</text>
    <text class="display-type title-en" x="284" y="246" font-size="122" textLength="522" lengthAdjust="spacingAndGlyphs">INKWAVE FRENZY</text>
    <text class="display-type title-en" x="36" y="348" font-size="118" textLength="556" lengthAdjust="spacingAndGlyphs">&amp; SKIN CRAFT EXPO</text>
  </g>

  <!-- Date -->
  <g class="date-block">
    <text class="cjk-type date-label" x="607" y="300" font-size="36">日期</text>
    <text class="display-type date-range" x="664" y="342" font-size="46" textLength="124" lengthAdjust="spacingAndGlyphs">9/2-9/4</text>
  </g>

  <!-- Emblem -->
  <g class="emblem">
    <circle class="badge-ring" cx="422" cy="678" r="294"/>
    <g class="ring-stars">
      <use href="#star-shape" class="badge-star" transform="rotate(0 422 678) translate(422 411)"/>
      <use href="#star-shape" class="badge-star" transform="rotate(15 422 678) translate(422 411)"/>
      <use href="#star-shape" class="badge-star" transform="rotate(30 422 678) translate(422 411)"/>
      <use href="#star-shape" class="badge-star" transform="rotate(45 422 678) translate(422 411)"/>
      <use href="#star-shape" class="badge-star" transform="rotate(60 422 678) translate(422 411)"/>
      <use href="#star-shape" class="badge-star" transform="rotate(75 422 678) translate(422 411)"/>
      <use href="#star-shape" class="badge-star" transform="rotate(90 422 678) translate(422 411)"/>
      <use href="#star-shape" class="badge-star" transform="rotate(105 422 678) translate(422 411)"/>
      <use href="#star-shape" class="badge-star" transform="rotate(120 422 678) translate(422 411)"/>
      <use href="#star-shape" class="badge-star" transform="rotate(135 422 678) translate(422 411)"/>
      <use href="#star-shape" class="badge-star" transform="rotate(150 422 678) translate(422 411)"/>
      <use href="#star-shape" class="badge-star" transform="rotate(165 422 678) translate(422 411)"/>
      <use href="#star-shape" class="badge-star" transform="rotate(180 422 678) translate(422 411)"/>
      <use href="#star-shape" class="badge-star" transform="rotate(195 422 678) translate(422 411)"/>
      <use href="#star-shape" class="badge-star" transform="rotate(210 422 678) translate(422 411)"/>
      <use href="#star-shape" class="badge-star" transform="rotate(225 422 678) translate(422 411)"/>
      <use href="#star-shape" class="badge-star" transform="rotate(240 422 678) translate(422 411)"/>
      <use href="#star-shape" class="badge-star" transform="rotate(255 422 678) translate(422 411)"/>
      <use href="#star-shape" class="badge-star" transform="rotate(270 422 678) translate(422 411)"/>
      <use href="#star-shape" class="badge-star" transform="rotate(285 422 678) translate(422 411)"/>
      <use href="#star-shape" class="badge-star" transform="rotate(300 422 678) translate(422 411)"/>
      <use href="#star-shape" class="badge-star" transform="rotate(315 422 678) translate(422 411)"/>
      <use href="#star-shape" class="badge-star" transform="rotate(330 422 678) translate(422 411)"/>
      <use href="#star-shape" class="badge-star" transform="rotate(345 422 678) translate(422 411)"/>
    </g>
    <g class="illustration" clip-path="url(#badge-window)" role="img"
       aria-label="Illustration: an orange hand rising from the bottom of the badge, gripping a yellow and cyan tattoo machine held up and to the left">
      <rect x="182" y="438" width="480" height="480" fill="var(--badge-fill)"/>
      <ellipse cx="444" cy="790" rx="150" ry="200" fill="url(#art-hand)"/>
      <ellipse cx="350" cy="600" rx="140" ry="115" fill="url(#art-machine)"/>
    </g>
    <circle class="badge-outline" cx="422" cy="678" r="240"/>
  </g>

  <!-- Venue -->
  <g class="venue">
    <text class="display-type venue-en" x="32" y="1036" font-size="58" textLength="792" lengthAdjust="spacingAndGlyphs">VENUE: SHANGHAI INTERNATIONAL BROCADE HALL</text>
    <text class="cjk-type venue-cn" x="204" y="1088" font-size="38" textLength="448" lengthAdjust="spacingAndGlyphs">地点：上海国际锦澜会馆</text>
  </g>

  <!-- Contact -->
  <g class="contact">
    <text class="contact-type" x="423" y="1142" text-anchor="middle">http://www.inkwavefrenzyfair.example</text>
    <text class="contact-type" x="423" y="1172" text-anchor="middle">Email: expo@inkwave-frenzy.example</text>
  </g>
</svg>
</body>
</html>
```